INNOVATIVE DESIGN NEEDED FOR FINANCIAL COMPANY

INTERNATIONAL FIRM IN HONG KONG NEEDS A MODERN BUSINESS CARD DESIGN. ONE SIDE ENGLISH OTHER SIDE IN CHINESE. WE ARE OPEN TO CHANGING FONTS AND COLOR. SHOULD BE A CARD THAT IS PROFESSIONAL DEALING WITH HIGH NET WORTH CLIENTELE. BOTH SIDES OF THE CARD WILL BE THE SAME, HOWEVER, THE WORDING ON ONE SIDE WILL BE ENGLISH AND THE OTHER SIDE IN CHINESE (CAN ASSIST IN THE LETTERING - CAN PROVIDE ONCE CARD DESIGN IS ACCEPTED.

Target Market(s)

Hong Kong/CHINA

Contact Information for Business Card

ATTRACTIVE MODERN

```html
<!DOCTYPE html>
<html lang="en">
<head>
<meta charset="utf-8">
<title>Willow Crest Asset Management – Business Card</title>
<link href="https://fonts.googleapis.com/css2?family=Roboto:wght@400;700;900&family=Noto+Sans+TC:wght@900&display=swap" rel="stylesheet">
<style>
  :root {
    --bg: #2b2b2b;
    --card-white: #f4f4f4;
    --green: #0fa07c;
    --green-dark: #0a8c6b;
    --grey-band: #8f8f8f;
    --ink: #3a3a3a;
    --ink-soft: #5a5a5a;
    --on-green: #ffffff;
  }
  * { box-sizing: border-box; margin: 0; padding: 0; }
  html, body { width: 1200px; height: 900px; overflow: hidden; }
  body {
    background: var(--bg);
    font-family: "Roboto", Arial, sans-serif;
    position: relative;
  }
  .business-card {
    position: absolute;
    left: 150px; top: 193px;
    width: 900px; height: 514px;
    background: var(--card-white);
    overflow: hidden;
  }
  .card-shapes { position: absolute; inset: 0; }
  .holder { position: absolute; left: 70px; top: 150px; }
  .holder-name {
    color: var(--green);
    font-weight: 900;
    font-size: 32px;
    letter-spacing: 1px;
    text-transform: uppercase;
    white-space: nowrap;
  }
  .holder-title {
    color: var(--ink-soft);
    font-size: 21px;
    margin-top: 2px;
  }
  .brand {
    position: absolute; left: 410px; top: 98px;
    display: flex; align-items: center; gap: 16px;
  }
  .brand-mark {
    width: 64px; height: 64px; border-radius: 50%;
    background: var(--green); flex: none;
  }
  .brand-name { color: var(--ink); font-weight: 900; white-space: nowrap; }
  .brand-name-zh {
    font-family: "Noto Sans TC", sans-serif;
    font-size: 33px; letter-spacing: 1px; line-height: 1.15;
  }
  .brand-name-en {
    font-family: "Roboto", Arial, sans-serif;
    font-size: 14px; letter-spacing: 2px; margin-top: 4px;
  }
  .contacts {
    position: absolute; left: 70px; top: 340px;
    list-style: none; color: var(--on-green);
    font-size: 19px; line-height: 30px;
  }
  .contacts li { display: flex; align-items: center; gap: 14px; white-space: nowrap; }
  .contacts svg { width: 18px; height: 18px; flex: none; }
  .address {
    position: absolute; right: 40px; top: 330px;
    color: var(--on-green); font-size: 19px; line-height: 26px; text-align: right;
    white-space: nowrap;
  }
</style>
</head>
<body>
  <article class="business-card">
    <svg class="card-shapes" viewBox="0 0 900 514" width="900" height="514" aria-hidden="true">
      <defs>
        <linearGradient id="greenBand" x1="0" y1="0" x2="1" y2="0">
          <stop offset="0" stop-color="#0a8c6b"/>
          <stop offset="1" stop-color="#0fa07c"/>
        </linearGradient>
      </defs>
      <polygon fill="url(#greenBand)"
        points="0,310 195,310 210,324 225,310 500,310 500,250 900,250 900,450 0,450"/>
      <rect class="grey-band" x="0" y="450" width="900" height="64" fill="#8f8f8f"/>
    </svg>

    <div class="holder">
      <div class="holder-name">Marcus Tenley</div>
      <div class="holder-title">General Manager</div>
    </div>

    <div class="brand">
      <span class="brand-mark"></span>
      <div class="brand-name">
        <div class="brand-name-zh">柳峰資產管理有限公司</div>
        <div class="brand-name-en">Willow Crest Asset Management Ltd</div>
      </div>
    </div>

    <ul class="contacts">
      <li>
        <svg viewBox="0 0 24 24"><path fill="#fff" d="M6.6 10.8c1.4 2.8 3.8 5.1 6.6 6.6l2.2-2.2c.3-.3.7-.4 1-.2 1.1.4 2.3.6 3.6.6.6 0 1 .4 1 1V20c0 .6-.4 1-1 1C10.6 21 3 13.4 3 4c0-.6.4-1 1-1h3.5c.6 0 1 .4 1 1 0 1.3.2 2.5.6 3.6.1.3 0 .7-.2 1z"/></svg>
        (852) 2761-4408
      </li>
      <li>
        <svg viewBox="0 0 24 24"><rect x="2" y="5" width="20" height="14" fill="#fff"/><path d="M2 5l10 8 10-8" fill="none" stroke="#0fa07c" stroke-width="2"/></svg>
        info@willowcrest.com
      </li>
      <li>
        <svg viewBox="0 0 24 24" fill="none" stroke="#fff" stroke-width="1.8"><circle cx="12" cy="12" r="9"/><ellipse cx="12" cy="12" rx="4" ry="9"/><path d="M3 12h18M5 7h14M5 17h14"/></svg>
        www.willowcrest.com
      </li>
    </ul>

    <p class="address">Units 5-6 Floor 9 Harbourview Tower West<br>Block 2 Canton Rd Tsim Sha Tsui KLN</p>
  </article>
</body>
</html>
```